Modern & Aesthetic Electrician Sign Design for Work Vehicle

Modern and aesthetic signage design for an electricians work vehicle. Including already designed logo, mobile number, ABN, licensing number and services offered. Preference is black background, symmetric design with logo centred, services offered at bottom of sign in smaller size font. Mobile number readable and big enough to standout without being too large.

Industry/Entity Type

Electrician

Font styles to use
Serif
Sans Serif

Colors
000000
ffffff
ec1f27

Requirements
Must have
• Logo
• Services Offered
• Mobile Number
• ABN
• License Number
• Black background

```html
<!DOCTYPE html>
<html lang="en">
<head>
<meta charset="utf-8">
<title>Halden Electrical – Vehicle Sign</title>
<link rel="stylesheet" href="https://fonts.googleapis.com/css2?family=Arimo:wght@400;700&display=swap">
<style>
  :root {
    --sign-black: #000000;
    --sign-white: #ffffff;
    --sign-red: #ec1f27;
    --page-bg: #ffffff;
  }
  html, body {
    margin: 0;
    padding: 0;
    width: 1200px;
    height: 694px;
    overflow: hidden;
    background: var(--page-bg);
  }
  .canvas {
    position: relative;
    width: 1200px;
    height: 694px;
    font-family: "Arimo", Arial, sans-serif;
  }
  .sign-panel {
    position: absolute;
    left: 58px;
    top: 122px;
    width: 1076px;
    height: 508px;
    background: var(--sign-black);
  }
  .brand-name {
    position: absolute;
    left: 124px;
    top: 226px;
    margin: 0;
    color: var(--sign-white);
    font-weight: 700;
    font-size: 84px;
    line-height: 1;
    white-space: nowrap;
  }
  .services,
  .license {
    position: absolute;
    left: 124px;
    margin: 0;
    color: var(--sign-white);
    font-weight: 400;
    font-size: 49px;
    line-height: 1;
    white-space: nowrap;
  }
  .services { top: 412px; letter-spacing: 0.3px; }
  .license { top: 478px; }
  .contact-band {
    position: absolute;
    left: 58px;
    top: 574px;
    width: 1076px;
    height: 56px;
    background: var(--sign-red);
  }
  .contact-band p {
    position: absolute;
    top: 12px;
    margin: 0;
    color: var(--sign-white);
    font-weight: 700;
    font-size: 34px;
    line-height: 1;
    white-space: nowrap;
  }
  .contact-address { left: 66px; }
  .contact-phone { right: 78px; }
</style>
</head>
<body>
<main class="canvas">
  <div class="sign-panel"></div>

  <h1 class="brand-name">HALDEN ELECTRICAL</h1>

  <p class="services">SERVICE OFFERED - SERVICE OFFERED</p>
  <p class="license">LICENSE NUMBER</p>

  <div class="contact-band">
    <p class="contact-address">ADDRESS: ABC</p>
    <p class="contact-phone">TEL: 0019005550142</p>
  </div>
</main>
</body>
</html>
```